Business Card

Yes I would like you to design me a business card with the logo you just made me

Industry/Entity Type

Business

Colors
33b7a4
00a990
333333
000000
757575
7f7f7f

```html
<!DOCTYPE html>
<html lang="en">
<head>
<meta charset="utf-8">
<title>Mara Velli Photography – Business Card</title>
<link rel="stylesheet" href="https://fonts.googleapis.com/css2?family=Open+Sans:wght@300;400;600&display=swap">
<style>
  :root {
    --teal: #33b7a4;
    --teal-deep: #00a990;
    --charcoal: #333333;
    --black: #000000;
    --grey: #757575;
    --grey-soft: #7f7f7f;
    --paper: #ffffff;
    --backdrop: #ecebe8;
  }
  * { margin: 0; padding: 0; box-sizing: border-box; }
  html, body {
    width: 1200px; height: 784px; overflow: hidden;
    background: var(--backdrop);
    font-family: "Open Sans", Arial, sans-serif;
  }
  .canvas {
    position: relative; width: 1200px; height: 784px;
    display: flex; align-items: center; justify-content: center; gap: 40px;
  }
  .card {
    position: relative; width: 550px; height: 314px; overflow: hidden;
    box-shadow: 0 6px 18px rgba(0,0,0,.18);
  }
  .card-back { background: var(--charcoal); }
  .card-front { background: var(--paper); }
  .card-art { position: absolute; inset: 0; width: 100%; height: 100%; }

  .brand {
    position: absolute; display: flex; flex-direction: column; align-items: center;
    font-weight: 300;
  }
  .brand-dot { width: 38px; height: 38px; border-radius: 50%; margin-bottom: 4px; }
  .brand-name { font-size: 40px; line-height: 1; letter-spacing: .5px; }
  .brand-line { font-size: 12px; letter-spacing: 6px; margin-top: 4px; text-transform: uppercase; }
  .card-back .brand { left: 0; right: 0; top: 88px; color: var(--paper); }
  .card-back .brand-dot { background: var(--paper); }
  .card-front .brand { left: 70px; top: 50px; width: 300px; color: var(--charcoal); }
  .card-front .brand-dot { background: var(--charcoal); }

  .holder {
    position: absolute; left: 150px; top: 236px; width: 172px; text-align: right;
  }
  .holder-name { color: var(--teal); font-weight: 600; font-size: 17px; line-height: 1.2; }
  .holder-role { color: var(--paper); font-size: 11px; }
  .divider {
    position: absolute; left: 333px; top: 204px; width: 1px; height: 86px;
    background: var(--grey-soft);
  }
  .contacts {
    position: absolute; left: 343px; top: 202px; list-style: none;
    color: var(--paper); font-size: 12px; line-height: 22px;
  }
  .contacts li { display: flex; align-items: center; gap: 6px; white-space: nowrap; }
  .contacts svg { width: 13px; height: 13px; flex: none; }
</style>
</head>
<body>
<main class="canvas">

  <section class="card card-back" aria-label="Card back">
    <div class="brand">
      <span class="brand-dot"></span>
      <span class="brand-name">mara velli</span>
      <span class="brand-line">photography</span>
    </div>
  </section>

  <section class="card card-front" aria-label="Card front">
    <svg class="card-art" viewBox="0 0 550 314" aria-hidden="true">
      <path d="M0,300 C180,290 330,200 550,30 L550,314 L0,314 Z" fill="var(--charcoal)"/>
      <path d="M270,218 C380,190 480,120 550,6 L550,30 C470,95 390,160 270,218 Z" fill="var(--teal-deep)"/>
    </svg>

    <div class="brand">
      <span class="brand-dot"></span>
      <span class="brand-name">mara velli</span>
      <span class="brand-line">photography</span>
    </div>

    <div class="holder">
      <p class="holder-name">Mara Velli</p>
      <p class="holder-role">Photographer</p>
    </div>
    <span class="divider"></span>

    <ul class="contacts">
      <li>
        <svg viewBox="0 0 14 14"><rect x="3" y="0.5" width="8" height="13" rx="1.5" fill="var(--teal)"/><rect x="4.5" y="2.5" width="5" height="7" fill="var(--charcoal)"/></svg>
        555-014-2290
      </li>
      <li>
        <svg viewBox="0 0 14 14"><rect x="0.5" y="2.5" width="13" height="9" rx="1" fill="var(--teal)"/><path d="M1,3 L7,8 L13,3" fill="none" stroke="var(--charcoal)" stroke-width="1.4"/></svg>
        maravelliphoto@example.com
      </li>
      <li>
        <svg viewBox="0 0 14 14"><rect x="1" y="1" width="12" height="12" rx="2" fill="var(--teal)"/></svg>
        maravelliphotography
      </li>
      <li>
        <svg viewBox="0 0 14 14"><path d="M7,1 L13.5,7 L11.5,7 L11.5,13 L8.5,13 L8.5,9 L5.5,9 L5.5,13 L2.5,13 L2.5,7 L0.5,7 Z" fill="var(--teal)"/></svg>
        Linden Vale Ma
      </li>
    </ul>
  </section>

</main>
</body>
</html>
```